KAV cards & more
Business cards, fax cover sheet, letterhead, envelopes, powerpoint slide template
Modern
Tad Willers
Owner
17 Lindgate Row Bedminster, NJ 07921
twkav@mailvane.net
Please integrate my already-completed company logo (attached) in a clean, modern design for business cards, Fax cover sheet, letterhead, envelopes, and powerpoint slide template

```html
<!DOCTYPE html>
<html lang="en">
<head>
<meta charset="utf-8">
<title>KAV Stationery Set</title>
<link href="https://fonts.googleapis.com/css2?family=Exo+2:wght@400;700;800&family=Open+Sans:wght@400;600&display=swap" rel="stylesheet">
<style>
:root{
  --green:#1e8a2c;
  --green-dark:#0f5e1c;
  --green-lime:#7cc21e;
  --green-pale:#e4f1e0;
  --ink:#444;
  --line:#bbb;
  --grey:#8d8d8d;
  --paper:#fff;
  --bg:#fff;
}
*{box-sizing:border-box;margin:0;padding:0}
html,body{width:1200px;height:504px;overflow:hidden;background:var(--bg)}
body{position:relative;font-family:"Open Sans",sans-serif;color:var(--ink)}
.sheet{position:absolute;background:var(--paper);box-shadow:0 1px 4px rgba(0,0,0,.25);overflow:hidden}
.brand{display:flex;align-items:center;gap:6px}
.brand-dot{width:22px;height:22px;border-radius:50%;background:var(--green)}
.brand-name{font-family:"Exo 2",sans-serif;font-weight:800;color:var(--green);font-size:22px;letter-spacing:3px}
.tagline{font-size:6px;color:var(--grey);margin-top:2px;margin-left:28px}
.foot-band{position:absolute;left:0;right:0;bottom:0;height:14px;background:linear-gradient(90deg,var(--green-dark),var(--green),var(--green-lime))}
.foot-text{position:absolute;left:0;right:0;bottom:16px;text-align:center;font-size:5.5px;color:var(--grey)}
.faint-mark{position:absolute;border-radius:50%;border:10px solid var(--green-pale)}

/* fax */
.fax{left:12px;top:12px;width:343px;height:463px}
.fax .brand{position:absolute;left:30px;top:26px}
.fax .tagline{position:absolute;left:30px;top:52px;margin:0}
.fax-title{position:absolute;right:36px;top:78px;font-family:"Exo 2",sans-serif;font-size:18px;color:var(--ink)}
.fax-fields{position:absolute;left:30px;right:30px;top:108px;display:grid;grid-template-columns:1fr 1fr;column-gap:24px;row-gap:10px;font-size:7px}
.field{display:flex;gap:6px;align-items:flex-end}
.field span{width:26px}
.field i{flex:1;border-bottom:1px solid var(--line);height:8px}
.fax-checks{position:absolute;left:30px;top:188px;display:flex;gap:12px;font-size:6px}
.fax-checks label{display:flex;align-items:center;gap:3px}
.fax-checks b{width:6px;height:6px;border:1px solid var(--ink)}
.fax-comments{position:absolute;left:30px;top:206px;font-size:6px}
.fax .faint-mark{left:205px;top:250px;width:100px;height:100px}

/* envelope */
.envelope{left:362px;top:12px;width:412px;height:276px}
.env-flap{position:absolute;left:0;top:0}
.env-flap .brand{position:absolute;left:50%;top:50px;transform:translateX(-50%)}
.env-flap .brand-dot{background:#fff}
.env-flap .brand-name{color:#fff;font-size:14px}
.env-return{position:absolute;left:30px;top:176px;font-size:5.5px;line-height:1.5;color:var(--green)}
.compliments{position:absolute;right:36px;bottom:22px;font-size:7px;letter-spacing:3px;color:#c8dcc4;text-transform:uppercase}
.envelope .faint-mark{right:40px;top:150px;width:80px;height:80px}

/* compliment slip */
.slip{left:362px;top:312px;width:412px;height:163px;background:linear-gradient(135deg,#fff 0%,#fff 12%,var(--green-lime) 40%,var(--green) 75%,var(--green-dark) 100%)}
.slip .left-panel{position:absolute;left:0;top:0;width:110px;height:100%;background:#fff}
.slip .brand{position:absolute;left:14px;top:16px}
.slip .brand-name{font-size:14px}
.slip .brand-dot{width:14px;height:14px}
.slip-addr{position:absolute;left:14px;bottom:20px;font-size:5.5px;line-height:1.5;color:var(--green)}
.slip .faint-mark{left:190px;top:18px;width:124px;height:124px;border-color:rgba(255,255,255,.22)}
.slip .compliments{color:rgba(255,255,255,.6)}

/* letterhead */
.letterhead{left:792px;top:12px;width:341px;height:463px}
.letterhead .brand{position:absolute;left:24px;top:26px}
.letterhead .tagline{position:absolute;left:24px;top:52px;margin:0}
.letterhead .faint-mark{left:215px;top:250px;width:100px;height:100px}

/* cards */
.card{left:1147px;width:48px;height:74px}
.card .brand{position:absolute;left:4px;top:6px;gap:2px}
.card .brand-dot{width:6px;height:6px}
.card .brand-name{font-size:7px;letter-spacing:1px}
.card-name{position:absolute;right:4px;top:22px;font-size:4px;text-align:right;line-height:1.3}
.card-wave{position:absolute;left:0;bottom:0}
.card-center{position:absolute;left:50%;top:50%;transform:translate(-50%,-50%);width:18px;height:18px;border-radius:50%}
.card-a{top:19px}
.card-b{top:115px}
.card-c{top:221px;background:linear-gradient(#9a9a9a,#6f6f6f)}
.card-d{top:326px;background:linear-gradient(160deg,var(--green),var(--green-dark))}
.card-e{top:410px;background:linear-gradient(160deg,var(--green-lime),#5fa51a)}
.card-c .card-center,.card-d .card-center{background:#fff}
.card-e .card-center{background:rgba(255,255,255,.35)}
</style>
</head>
<body>

<section class="sheet fax">
  <div class="brand"><span class="brand-dot"></span><span class="brand-name">KAV</span></div>
  <p class="tagline">Home Renovation Experts</p>
  <h1 class="fax-title">FAX</h1>
  <div class="fax-fields">
    <div class="field"><span>To:</span><i></i></div>
    <div class="field"><span>From:</span><i></i></div>
    <div class="field"><span>Fax:</span><i></i></div>
    <div class="field"><span>Pages:</span><i></i></div>
    <div class="field"><span>Phone:</span><i></i></div>
    <div class="field"><span>Date:</span><i></i></div>
    <div class="field"><span>Re:</span><i></i></div>
    <div class="field"><span>CC:</span><i></i></div>
  </div>
  <div class="fax-checks">
    <label><b></b>Urgent</label><label><b></b>For Review</label><label><b></b>Please Comment</label><label><b></b>Please Reply</label>
  </div>
  <p class="fax-comments">Comments:</p>
  <div class="faint-mark"></div>
  <p class="foot-text">17 Lindgate Row, Bedminster, NJ 07921 · Tel 908 555 0142 · twkav@mailvane.net</p>
  <div class="foot-band"></div>
</section>

<section class="sheet envelope">
  <svg class="env-flap" width="412" height="128" viewBox="0 0 412 128">
    <defs><linearGradient id="flapGrad" x1="0" y1="0" x2="0" y2="1"><stop offset="0" stop-color="#0f5e1c"/><stop offset="1" stop-color="#2a9a34"/></linearGradient></defs>
    <path d="M0 0H412V78Q300 86 206 120Q112 86 0 78Z" fill="url(#flapGrad)"/>
    <path d="M0 78Q112 86 206 120Q300 86 412 78" fill="none" stroke="#7cc21e" stroke-width="2"/>
  </svg>
  <div class="env-flap" style="width:412px;height:128px"><div class="brand"><span class="brand-dot"></span><span class="brand-name">KAV</span></div></div>
  <p class="env-return">17 Lindgate Row<br>Bedminster, NJ 07921</p>
  <div class="faint-mark"></div>
  <p class="compliments">With Compliments</p>
</section>

<section class="sheet slip">
  <div class="left-panel"></div>
  <div class="brand"><span class="brand-dot"></span><span class="brand-name">KAV</span></div>
  <p class="slip-addr">17 Lindgate Row<br>Bedminster, NJ 07921</p>
  <div class="faint-mark"></div>
  <p class="compliments">With Compliments</p>
</section>

<section class="sheet letterhead">
  <div class="brand"><span class="brand-dot"></span><span class="brand-name">KAV</span></div>
  <p class="tagline">Home Renovation Experts</p>
  <div class="faint-mark"></div>
  <p class="foot-text">17 Lindgate Row, Bedminster, NJ 07921 · Tel 908 555 0142 · twkav@mailvane.net</p>
  <div class="foot-band"></div>
</section>

<section class="sheet card card-a">
  <div class="brand"><span class="brand-dot"></span><span class="brand-name">KAV</span></div>
  <p class="card-name"><strong>Tad Willers</strong><br>Owner</p>
  <svg class="card-wave" width="48" height="22" viewBox="0 0 48 22"><path d="M0 10Q24 22 48 4V22H0Z" fill="#1e8a2c"/></svg>
</section>
<section class="sheet card card-b">
  <div class="brand"><span class="brand-dot"></span><span class="brand-name">KAV</span></div>
  <p class="card-name"><strong>Tad Willers</strong><br>Owner</p>
  <svg class="card-wave" width="48" height="22" viewBox="0 0 48 22"><path d="M0 14Q24 4 48 12V22H0Z" fill="#7cc21e"/></svg>
</section>
<section class="sheet card card-c"><span class="card-center"></span></section>
<section class="sheet card card-d"><span class="card-center"></span></section>
<section class="sheet card card-e" style="height:62px"><span class="card-center"></span></section>

</body>
</html>
```